Etiquetas para platos preparados de la marca El Fogón Verde

Necesito el diseño de una belly band o etiquetas para productos cocinados. En ella debe aparecer la siguiente información: el logo de la marca,
Símbolos con la siguiente info: refrigerado entre 2º-4º, pincha el plástico que lo cubre, imagen microondas 3:00, disfruta.
Además necesito que la etiqueta tenga en la parte frontal una zona donde podamos modificar e ir añadiendo el nombre del producto en concreto y en la parte trasera una zona destinada también a los valores nutricionales personalizable.
Por último necesitamos que las etiquetas estén diseñadas en 6 colores diferentes para poder diferenciar entre diferentes categorías (ensaladas, carnes, pescados, postres, ECO...).
Los tamaños de los envases sobre los que debe ir el belly band es el siguiente:
-Formato 1: 180x180x35mm
-Formato 2: 168x128x35mm
-Formato 3: belly band de 30cm de largo

Target Market(s)

Producto expuesto es vitrinas expositoras de supermercados

Industry/Entity Type

Alimentación

Font styles to use
Sans Serif
Other font styles liked:
• Cocomat y Poppins

Requirements
Must have
• Atractivo visualmente. Fuentes empleadas Cocomat y Montserrat
Nice to have
• Los colores para diferenciar categorías y espacio para poder incluir nosotros el nombre de cada producto. Además un espacio que ponga Origen personalizable también y un logo que ponga casero 100%

```html
<!DOCTYPE html>
<html lang="es">
<head>
<meta charset="utf-8">
<title>El Fogón Verde – Belly bands por categoría</title>
<link href="https://fonts.googleapis.com/css2?family=Josefin+Sans:wght@300&family=Poppins:wght@400;600;700;800&display=swap" rel="stylesheet">
<style>
  :root{
    --canvas:#adadad;
    --white:#ffffff;
    --ink:#2e4147;
    --salads:#8fb840;
    --meats:#c24527;
    --fish:#0aa7c6;
    --desserts:#b398c2;
    --eco:#71873a;
    --meals:#d4a22a;
    --shade:rgba(0,0,0,.2);
  }
  *{margin:0;padding:0;box-sizing:border-box}
  html,body{width:1200px;height:1200px;overflow:hidden;background:var(--canvas)}
  .sheet{position:absolute;left:375px;top:43px;width:409px;height:1114px;background:var(--white)}
  .band{position:relative;height:184.5px;--c:var(--salads)}
  .band--salads{--c:var(--salads)}
  .band--meats{--c:var(--meats)}
  .band--fish{--c:var(--fish)}
  .band--desserts{--c:var(--desserts)}
  .band--eco{--c:var(--eco)}
  .band--meals{--c:var(--meals)}
  .stripe{position:absolute;left:0;right:0;height:3px;background:var(--c)}
  .stripe--top{top:0}
  .stripe--bottom{top:163px}
  .block{position:absolute;left:0;right:0;top:12.4px;height:141.6px;background:var(--c)}
  .info-box{position:absolute;top:34px;width:65px;height:73px;border-radius:4px;background:var(--shade);color:var(--white);font-family:"Poppins",sans-serif;padding:9px 4px 0 3.5px}
  .info-box--ingredients{left:14px}
  .info-box--nutrition{right:14px;padding-top:8px}
  .info-title{font-weight:700;font-size:6.6px;line-height:1.1}
  .info-box--nutrition .info-title{font-size:4.4px}
  .info-text{font-size:3.1px;line-height:1.35;margin-top:2px;opacity:.95}
  .weight{position:absolute;left:4px;bottom:6px;font-weight:700;font-size:6.4px}
  .recycle{position:absolute;right:5px;bottom:4px;width:14px;height:14px}
  .card{position:absolute;left:135px;top:5.6px;width:139px;height:130px;border-radius:19px;background:var(--white);text-align:center;color:var(--ink)}
  .brand{font-family:"Josefin Sans",sans-serif;font-weight:300;font-size:17px;line-height:1.05;letter-spacing:.5px;text-transform:uppercase;margin-top:16px}
  .category{display:inline-block;margin-top:9px;min-width:99px;padding:3px 8px 2px;background:var(--c);color:var(--white);font-family:"Poppins",sans-serif;font-weight:800;font-size:12px;letter-spacing:2.4px;line-height:14px;border-radius:2px}
  .category--wide{min-width:127px;letter-spacing:1.4px;padding:3px 4px 2px}
  .category--meals{letter-spacing:.3px}
  .steps{display:flex;justify-content:center;gap:4px;margin-top:14px;font-family:"Poppins",sans-serif;font-size:3.6px;line-height:1.2;color:var(--ink)}
  .step{display:flex;flex-direction:column;align-items:center;width:20px}
  .step svg{width:11px;height:11px;margin-bottom:1.5px}
</style>
</head>
<body>
<svg width="0" height="0" style="position:absolute">
  <defs>
    <symbol id="icon-recycle" viewBox="0 0 20 20"><circle cx="10" cy="10" r="8.8" fill="none" stroke="#fff" stroke-width="1.2"/><path d="M7 8.5l2-3 2 3M13.5 10l1.5 3h-4M6.5 13.2l-1.6-2.8 2.1-1.5" fill="none" stroke="#fff" stroke-width="1.3" stroke-linejoin="round"/></symbol>
    <symbol id="icon-fridge" viewBox="0 0 12 12"><rect x="2" y="1" width="2" height="7" rx="1" fill="none" stroke="#2e4147" stroke-width=".7"/><circle cx="3" cy="9.5" r="1.6" fill="#2e4147"/><text x="6" y="4" font-size="2.6" font-family="Poppins,sans-serif" fill="#2e4147">ºC</text><text x="5.5" y="8" font-size="2.2" font-family="Poppins,sans-serif" fill="#2e4147">2º-4º</text></symbol>
    <symbol id="icon-pierce" viewBox="0 0 12 12"><path d="M6 2l4 4-4 4-4-4z" fill="none" stroke="#2e4147" stroke-width=".7"/><path d="M3 9l3-3" stroke="#2e4147" stroke-width=".7"/></symbol>
    <symbol id="icon-microwave" viewBox="0 0 12 12"><rect x="1" y="3" width="10" height="6.5" fill="none" stroke="#2e4147" stroke-width=".7"/><rect x="2" y="4" width="6" height="4.5" fill="none" stroke="#2e4147" stroke-width=".5"/><text x="2.6" y="7.1" font-size="2" font-family="Poppins,sans-serif" fill="#2e4147">3:00</text><path d="M9 4.5h1.2M9 6h1.2M9 7.5h1.2" stroke="#2e4147" stroke-width=".5"/></symbol>
    <symbol id="icon-smile" viewBox="0 0 12 12"><circle cx="6" cy="6" r="4.3" fill="none" stroke="#2e4147" stroke-width=".8"/><circle cx="4.5" cy="5" r=".6" fill="#2e4147"/><circle cx="7.5" cy="5" r=".6" fill="#2e4147"/><path d="M4 7a2.4 2.4 0 004 0" fill="none" stroke="#2e4147" stroke-width=".7"/></symbol>
  </defs>
</svg>

<main class="sheet">
  <section class="band band--salads">
    <div class="stripe stripe--top"></div>
    <div class="block">
      <div class="info-box info-box--ingredients"><p class="info-title">INGREDIENTES</p><p class="info-text">Lorem ipsum dolor sit amet, consectetuer adipiscing elit, sed diam nonummy nibh euismod tincidunt ut laoreet.</p><p class="weight">500G</p><svg class="recycle"><use href="#icon-recycle"/></svg></div>
      <div class="card"><p class="brand">El Fogón<br>Verde</p><p class="category">SALADS</p>
        <div class="steps"><div class="step"><svg><use href="#icon-fridge"/></svg>Refrigerado Entre</div><div class="step"><svg><use href="#icon-pierce"/></svg>Pincha El Plástico Que Lo Cubre</div><div class="step"><svg><use href="#icon-microwave"/></svg>Imagen Microondas</div><div class="step"><svg><use href="#icon-smile"/></svg>Disfruta</div></div></div>
      <div class="info-box info-box--nutrition"><p class="info-title">VALORES NUTRICIONALES</p><p class="info-text">Lorem ipsum dolor sit amet, consectetuer adipiscing elit, sed diam nonummy nibh euismod tincidunt ut laoreet.</p></div>
    </div>
    <div class="stripe stripe--bottom"></div>
  </section>

  <section class="band band--meats">
    <div class="stripe stripe--top"></div>
    <div class="block">
      <div class="info-box info-box--ingredients"><p class="info-title">INGREDIENTES</p><p class="info-text">Lorem ipsum dolor sit amet, consectetuer adipiscing elit, sed diam nonummy nibh euismod tincidunt ut laoreet.</p><p class="weight">500G</p><svg class="recycle"><use href="#icon-recycle"/></svg></div>
      <div class="card"><p class="brand">El Fogón<br>Verde</p><p class="category">MEATS</p>
        <div class="steps"><div class="step"><svg><use href="#icon-fridge"/></svg>Refrigerado Entre</div><div class="step"><svg><use href="#icon-pierce"/></svg>Pincha El Plástico Que Lo Cubre</div><div class="step"><svg><use href="#icon-microwave"/></svg>Imagen Microondas</div><div class="step"><svg><use href="#icon-smile"/></svg>Disfruta</div></div></div>
      <div class="info-box info-box--nutrition"><p class="info-title">VALORES NUTRICIONALES</p><p class="info-text">Lorem ipsum dolor sit amet, consectetuer adipiscing elit, sed diam nonummy nibh euismod tincidunt ut laoreet.</p></div>
    </div>
    <div class="stripe stripe--bottom"></div>
  </section>

  <section class="band band--fish">
    <div class="stripe stripe--top"></div>
    <div class="block">
      <div class="info-box info-box--ingredients"><p class="info-title">INGREDIENTES</p><p class="info-text">Lorem ipsum dolor sit amet, consectetuer adipiscing elit, sed diam nonummy nibh euismod tincidunt ut laoreet.</p><p class="weight">500G</p><svg class="recycle"><use href="#icon-recycle"/></svg></div>
      <div class="card"><p class="brand">El Fogón<br>Verde</p><p class="category">FISH</p>
        <div class="steps"><div class="step"><svg><use href="#icon-fridge"/></svg>Refrigerado Entre</div><div class="step"><svg><use href="#icon-pierce"/></svg>Pincha El Plástico Que Lo Cubre</div><div class="step"><svg><use href="#icon-microwave"/></svg>Imagen Microondas</div><div class="step"><svg><use href="#icon-smile"/></svg>Disfruta</div></div></div>
      <div class="info-box info-box--nutrition"><p class="info-title">VALORES NUTRICIONALES</p><p class="info-text">Lorem ipsum dolor sit amet, consectetuer adipiscing elit, sed diam nonummy nibh euismod tincidunt ut laoreet.</p></div>
    </div>
    <div class="stripe stripe--bottom"></div>
  </section>

  <section class="band band--desserts">
    <div class="stripe stripe--top"></div>
    <div class="block">
      <div class="info-box info-box--ingredients"><p class="info-title">INGREDIENTES</p><p class="info-text">Lorem ipsum dolor sit amet, consectetuer adipiscing elit, sed diam nonummy nibh euismod tincidunt ut laoreet.</p><p class="weight">500G</p><svg class="recycle"><use href="#icon-recycle"/></svg></div>
      <div class="card"><p class="brand">El Fogón<br>Verde</p><p class="category">DESSERTS</p>
        <div class="steps"><div class="step"><svg><use href="#icon-fridge"/></svg>Refrigerado Entre</div><div class="step"><svg><use href="#icon-pierce"/></svg>Pincha El Plástico Que Lo Cubre</div><div class="step"><svg><use href="#icon-microwave"/></svg>Imagen Microondas</div><div class="step"><svg><use href="#icon-smile"/></svg>Disfruta</div></div></div>
      <div class="info-box info-box--nutrition"><p class="info-title">VALORES NUTRICIONALES</p><p class="info-text">Lorem ipsum dolor sit amet, consectetuer adipiscing elit, sed diam nonummy nibh euismod tincidunt ut laoreet.</p></div>
    </div>
    <div class="stripe stripe--bottom"></div>
  </section>

  <section class="band band--eco">
    <div class="stripe stripe--top"></div>
    <div class="block">
      <div class="info-box info-box--ingredients"><p class="info-title">INGREDIENTES</p><p class="info-text">Lorem ipsum dolor sit amet, consectetuer adipiscing elit, sed diam nonummy nibh euismod tincidunt ut laoreet.</p><p class="weight">500G</p><svg class="recycle"><use href="#icon-recycle"/></svg></div>
      <div class="card"><p class="brand">El Fogón<br>Verde</p><p class="category category--wide">ECO/ORGANIC</p>
        <div class="steps"><div class="step"><svg><use href="#icon-fridge"/></svg>Refrigerado Entre</div><div class="step"><svg><use href="#icon-pierce"/></svg>Pincha El Plástico Que Lo Cubre</div><div class="step"><svg><use href="#icon-microwave"/></svg>Imagen Microondas</div><div class="step"><svg><use href="#icon-smile"/></svg>Disfruta</div></div></div>
      <div class="info-box info-box--nutrition"><p class="info-title">VALORES NUTRICIONALES</p><p class="info-text">Lorem ipsum dolor sit amet, consectetuer adipiscing elit, sed diam nonummy nibh euismod tincidunt ut laoreet.</p></div>
    </div>
    <div class="stripe stripe--bottom"></div>
  </section>

  <section class="band band--meals">
    <div class="stripe stripe--top"></div>
    <div class="block">
      <div class="info-box info-box--ingredients"><p class="info-title">INGREDIENTES</p><p class="info-text">Lorem ipsum dolor sit amet, consectetuer adipiscing elit, sed diam nonummy nibh euismod tincidunt ut laoreet.</p><p class="weight">500G</p><svg class="recycle"><use href="#icon-recycle"/></svg></div>
      <div class="card"><p class="brand">El Fogón<br>Verde</p><p class="category category--wide category--meals">PREPARED MEALS</p>
        <div class="steps"><div class="step"><svg><use href="#icon-fridge"/></svg>Refrigerado Entre</div><div class="step"><svg><use href="#icon-pierce"/></svg>Pincha El Plástico Que Lo Cubre</div><div class="step"><svg><use href="#icon-microwave"/></svg>Imagen Microondas</div><div class="step"><svg><use href="#icon-smile"/></svg>Disfruta</div></div></div>
      <div class="info-box info-box--nutrition"><p class="info-title">VALORES NUTRICIONALES</p><p class="info-text">Lorem ipsum dolor sit amet, consectetuer adipiscing elit, sed diam nonummy nibh euismod tincidunt ut laoreet.</p></div>
    </div>
    <div class="stripe stripe--bottom"></div>
  </section>
</main>
</body>
</html>
```